Raw Food & Health Coach Needs a Clutch Coupon

I need a clutch coupon for a raw food & health coaching business based in Washington, DC called Cora Penwick, LLC. I help ladies and gents on the go who want to support their bodies to stay healthy or prevent/correct disease so they can live extraordinary lives while deeply serving the world. My services include individual coaching, (online) group coaching, and corporate wellness coaching.

I would like to create a clutch coupon to give to referral partners who in turn will give them to their clients. So far I have two referral partners in mind: Marcus Elvey Salon & Spa; and Colon Hydrotherapist Wendy Tasbrook.

Marcus Elvey Salon & Spa will be having an event on Thursday, September 12, 2013, during which time their clients who get a hair cut will receive a complimentary Velunique (hair) Treatment & a complimentary Radiant Through and Through Planning Hour with me.

I would like to see designs that use 2-4 colors, including a bit of green. The final design should communicate beauty/health from the inside out and boundless energy to enjoy an extraordinary life. It should be natural yet elegant/classy.

Designers are currently working on my business logo. The logo design project has not yet been completed. Once it completes, I will send the logo design to you and request that you incorporate the logo into your coupon design.

IMPORTANT: I need to select a winning design on Wed, Sept 11, 2013, and get the source files from the designer within 24 hours (before Thursday, Sept 12 MORNING); so that I have time to adjust any text and take it to the printer in order to distribute the coupon later that afternoon. I will need the source files urgently (within the next 24 hours).

Then after the event the designer will make the changes on the design for me incorporating my logo for use with multiple referral partners. I will approve the Payment when I have finalized the design

To repeat, I must have the winning design on September 11 (or Sept 12 morning at the latest).

IMPORTANT: Refer to uploaded Referral Partner Clutch Coupon SAMPLE to give you an idea of the layout I'd like, but PLEASE don't let it stifle YOUR creativity.
Updates

The focus should be on the Free Radiant Through and Through Planning Hour, not on me.

 

I think I’d prefer a white background and black text, unless you can convince me otherwise by showing me a beautiful design.

 

Ensure there is space between paragraphs.

 

Somehow differentiate my free gift (Wellbeing Guard Starter Kit), phone and URL at the bottom on the back. While it would be nice to include my free gift, I may have to leave out if it won’t fit on the coupon.

Target Market(s)

The audience is busy, heart-centered/socially responsible professional men and women on the go who hardly have time for self-care, but who will pay for holistic services (alternative therapies) to enhance their beauty/health so that they can perform their best while deeply serving the world without getting sick or having to endure toxic therapies like surgery, chemotherapy, radiation, and pills.

Industry/Entity Type

Printer

Requirements
Must have
• 2-4 colors, including a little green

Dimensions: approx. 2.25 inches x 5.25 inches.

Text from the uploaded file. Note: I'm not sure if all the text I've provided will fit nicely on the back of the coupon. If no then please increase the dimensions as little as possible.

The front of the coupon designed horizontally, and the back designed vertically.
Nice to have
• I'm open to your using illustrations or photos of the raw food and/or lifestyle tools that I use with clients in my business, such as green juice, (leafy) green veggies, cucumbers, lemons, berries, green smoothies, superfoods, movement/exercise, self-care...

I also like the idea of including a face in the design. When I’ve surveyed in the past people have related better to a face than just to a bowl of veggies or fruit.
Should not have
• the colors orange or red, or florescent colors.

```html
<!DOCTYPE html>
<html lang="en">
<head>
<meta charset="utf-8">
<title>Cora Penwick – Clutch Coupon</title>
<link rel="stylesheet" href="https://fonts.googleapis.com/css2?family=Source+Sans+3:wght@400;600;700&display=swap">
<style>
  :root {
    --board: #c9c7c8;
    --paper: #ffffff;
    --sky: #45c3ef;
    --ocean-deep: #1f4f5c;
    --ocean-mid: #2e7f96;
    --leaf: #5a9a2e;
    --leaf-soft: #e9f3df;
    --ink: #1b1b1b;
    --white: #ffffff;
    --shadow: rgba(0,0,0,0.35);
  }
  * { box-sizing: border-box; margin: 0; padding: 0; }
  html, body { width: 1200px; height: 800px; overflow: hidden; }
  body {
    background: var(--board);
    font-family: "Source Sans 3", "Myriad Pro", Arial, sans-serif;
    position: relative;
  }

  /* ---------- Front of coupon ---------- */
  .coupon-front {
    position: absolute; left: 43px; top: 60px; width: 708px; height: 305px;
    background: var(--paper);
    box-shadow: 2px 3px 6px var(--shadow);
    overflow: hidden;
  }
  .front-portrait {
    position: absolute; left: 0; top: 0; width: 420px; height: 305px;
    background:
      linear-gradient(90deg, rgba(255,255,255,0) 55%, var(--paper) 100%),
      radial-gradient(ellipse at 45% 45%, #e9d2bf 0%, #b89a86 30%, #6f95a8 60%, #7fc6e4 90%);
  }
  .front-accent {
    position: absolute; left: 0; bottom: 0; width: 708px; height: 6px;
    background: var(--leaf);
  }
  .front-name {
    position: absolute; left: 147px; top: 27px;
    color: var(--white); font-weight: 600; font-size: 20px; letter-spacing: 4px;
  }
  .front-title {
    position: absolute; left: 362px; top: 27px; width: 320px;
    color: var(--leaf); font-weight: 600; font-size: 20px; letter-spacing: 4.5px;
    border-bottom: 2px solid var(--leaf); line-height: 24px; padding-bottom: 1px;
  }
  .front-offer {
    position: absolute; left: 372px; top: 55px; list-style: none;
    color: var(--ink); font-size: 15px; line-height: 18px;
  }
  .front-offer li::before { content: "»"; margin-right: 10px; color: var(--leaf); }
  .front-divider {
    position: absolute; left: 362px; width: 320px; text-align: center;
    color: var(--leaf); font-size: 17px;
  }
  .front-detail {
    position: absolute; left: 362px; color: var(--ink); font-size: 15.5px; line-height: 20px;
  }
  .front-value {
    position: absolute; left: 362px; top: 167px;
    color: var(--leaf); font-weight: 700; font-size: 19px;
  }
  .front-url {
    position: absolute; left: 362px; top: 258px;
    color: var(--ink); font-weight: 700; font-size: 17px;
  }

  /* ---------- Back of coupon ---------- */
  .coupon-back {
    position: absolute; left: 834px; top: 58px; width: 303px; height: 707px;
    background: var(--paper);
    box-shadow: 2px 3px 6px var(--shadow);
    color: var(--ink);
    overflow: hidden;
  }
  .back-band {
    position: absolute; left: 0; top: 0; width: 303px; height: 6px;
    background: var(--leaf);
  }
  .back-heading {
    position: absolute; left: 26px; top: 14px; width: 250px;
    color: var(--leaf);
    font-weight: 700; font-size: 17px; letter-spacing: 3px; line-height: 18px;
    border-bottom: 2px solid var(--leaf);
  }
  .back-copy {
    position: absolute; left: 26px; top: 38px; width: 252px;
    font-size: 11px; line-height: 13.5px; text-align: justify;
  }
  .back-copy h3 { font-size: 11px; font-weight: 700; color: var(--leaf); }
  .back-copy p + h3 { margin-top: 13px; }
  .benefit-list { list-style: none; margin: 17px 0 0 8px; }
  .benefit-list li { padding-left: 18px; text-indent: -18px; text-align: left; }
  .benefit-list li::before { content: "»"; display: inline-block; width: 18px; text-indent: 0; color: var(--leaf); }
  .benefit-list + h3 { margin-top: 14px; }
  .coach-photo {
    position: absolute; left: 26px; top: 574px; width: 118px; height: 116px;
    background: radial-gradient(ellipse at 50% 45%, #c99b80 0%, #7a4f3c 45%, #9a8570 80%, #b5a894 100%);
  }
  .back-contact {
    position: absolute; left: 159px; top: 595px; width: 120px;
    font-size: 11px; line-height: 13.5px;
  }
  .back-contact strong { font-weight: 700; color: var(--leaf); }
</style>
</head>
<body>

<section class="coupon-front" aria-label="Coupon front">
  <div class="front-portrait" role="img" aria-label="Portrait photo of a relaxed young man in a white shirt"></div>
  <div class="front-name">CORA PENWICK</div>
  <h1 class="front-title">TREAT YOURSELF</h1>
  <ul class="front-offer">
    <li>Free Radiant Through and Through</li>
    <li>Planning Hour with Certified Raw</li>
    <li>Food &amp; Health Coach, Cora Penwick</li>
  </ul>
  <div class="front-divider" style="top:113px">/</div>
  <p class="front-detail" style="top:142px">30 minutes, focused entirely on you.</p>
  <p class="front-value">(A $50 VALUE, FREE)</p>
  <div class="front-divider" style="top:194px">/</div>
  <p class="front-detail" style="top:220px">Compliments of Marcus Elvey Salon &amp; Spa<br>To schedule your appointment, simply go to:</p>
  <p class="front-url">HTTP://LNK.CPW/RTTH.</p>
  <div class="front-accent"></div>
</section>

<section class="coupon-back" aria-label="Coupon back">
  <div class="back-band"></div>
  <h2 class="back-heading">Q. &amp; A.</h2>
  <div class="back-copy">
    <h3>What is Raw Food &amp; Health Coaching?</h3>
    <p>Raw food coaching helps you go or stay raw to the level that you truly desire. Health coaching helps you connect the dots between what you eat and how you feel. You’ll know how to detoxify and oxygenate your body, alkalize your pH, and delight in what you eat like never before – without restriction.</p>
    <h3>WHO BENEFITS FROM THIS WORK?</h3>
    <p>Smart, service-oriented ladies and gents on the go who want to enable their bodies to prevent/ correct disease and create energy so they can live extraordinary lives without crashing, getting sick or neglecting their own health. Raw food is literally for everyone, but the degree to which someone goes raw and for what duration is a very personal decision. This is about what works for you, what feels right for you and what get you to where you want to be. Generally speaking, raw food &amp; health coaching is great for anyone who wants to…</p>
    <ul class="benefit-list">
      <li>Correct or prevent a serious disease</li>
      <li>Look and/or feel better</li>
      <li>Look/feel 10 years younger</li>
      <li>Gravitate to their perfect body weight without dieting</li>
      <li>Double their energy</li>
      <li>Reduce their cravings</li>
      <li>Detox their body</li>
      <li>Think more clearly</li>
      <li>Get a lot done without having a lot of time</li>
      <li>Feel happier/improve their mood</li>
    </ul>
    <h3>What happens in the initial consultation?</h3>
    <p>This 30 minute phone call is a time to discuss your unique health challenge(s) and desires. I guarantee you’ll walk away with at least 1 aha about why you’re stuck and more clarity about what it’ll take to put you on the fast track to where you want to go.</p>
  </div>
  <div class="coach-photo" role="img" aria-label="Portrait photo of the coach"></div>
  <p class="back-contact">To schedule your appointment, simply go to: <strong>http://lnk.cpw/RTTH.</strong><br><strong>202-555-0147</strong><br><strong>corapenwick.com</strong></p>
</section>

</body>
</html>
```